Brisk Ember - Stock Certificate

We need a custom designed stock certificate that represents the look of our company logo but also have a cool look compared to a standard stock certificate. We thinking we want the logo in gold. Our website is https://www.briskemberusa.example.

We are wanting the certificate to look very professional and really cool, we have sales agents that work for the company and we are creating a program by which the sales agents can gain ownership in the company. So the certificates need to have a very cool appeal and that provides a sense of pride in owning "Units" in Brisk Ember.

Reason: Extending so other board members can vote as well, thank you all!

Target Market(s)

Stock/Shareholders

Industry/Entity Type

It Company

Font styles to use
Script

Requirements
Must have
• Must look like a stock certificate, must use our logo which the psd file for it was attached.
Nice to have
• Nice to have the logo in gold

```html
<!DOCTYPE html>
<html lang="en">
<head>
<meta charset="utf-8">
<title>Brisk Ember – Stock Certificate</title>
<link href="https://fonts.googleapis.com/css2?family=UnifrakturCook:wght@700&family=Great+Vibes&family=Arimo:wght@400&family=Open+Sans:ital@1&display=swap" rel="stylesheet">
<style>
  :root {
    --page-bg: #d9d9d9;
    --paper: #0a0a0a;
    --land-light: #3a3a3a;
    --land-dark: #151515;
    --ink: #ffffff;
    --frame-orange: #ff5a00;
    --frame-yellow: #ffd21a;
    --gold-deep: #e06a00;
    --gold-light: #ffc640;
    --rule: #ffffff;
  }
  html, body {
    margin: 0;
    width: 930px;
    height: 1200px;
    overflow: hidden;
    background: var(--page-bg);
  }
  .stage {
    position: relative;
    width: 930px;
    height: 1200px;
  }
  .certificate {
    position: absolute;
    left: 0;
    top: 272px;
    width: 1162px;
    height: 820px;
    transform: scale(0.8);
    transform-origin: 0 0;
    background: var(--paper);
    overflow: hidden;
    font-family: "Arimo", Arial, sans-serif;
    color: var(--ink);
  }
  .world-map {
    position: absolute;
    inset: 0;
    background:
      radial-gradient(ellipse 22% 30% at 20% 28%, var(--land-light), transparent 70%),
      radial-gradient(ellipse 12% 26% at 30% 70%, var(--land-light), transparent 70%),
      radial-gradient(ellipse 30% 24% at 62% 30%, var(--land-light), transparent 70%),
      radial-gradient(ellipse 12% 22% at 52% 58%, var(--land-light), transparent 70%),
      radial-gradient(ellipse 10% 10% at 86% 72%, var(--land-light), transparent 70%),
      linear-gradient(180deg, var(--land-dark), var(--paper));
    opacity: 0.85;
  }
  .frame {
    position: absolute;
    inset: 0;
  }
  .title {
    position: absolute;
    left: 0;
    right: 0;
    top: 78px;
    margin: 0;
    text-align: center;
    font-family: "UnifrakturCook", serif;
    font-weight: 700;
    font-size: 86px;
    line-height: 1;
    padding-left: 0;
    letter-spacing: 1px;
  }
  .brand {
    position: absolute;
    left: 110px;
    top: 548px;
    display: flex;
    align-items: center;
    gap: 12px;
    font-size: 38px;
    color: var(--ink);
  }
  .brand-dot {
    width: 18px;
    height: 18px;
    border-radius: 50%;
    background: var(--frame-orange);
  }
  .body-copy {
    position: absolute;
    left: 355px;
    width: 750px;
    text-align: center;
    font-size: 19px;
    line-height: 25px;
    margin: 0;
  }
  .certifies { top: 242px; }
  .holder {
    position: absolute;
    left: 500px;
    top: 300px;
    width: 462px;
    height: 86px;
    border-bottom: 1.5px solid var(--rule);
    text-align: center;
    font-family: "Great Vibes", cursive;
    font-size: 64px;
    line-height: 86px;
    background: linear-gradient(90deg, var(--gold-deep), var(--gold-light) 60%, var(--gold-deep));
    -webkit-background-clip: text;
    background-clip: text;
    color: transparent;
  }
  .holder-rule {
    position: absolute;
    left: 500px;
    top: 387px;
    width: 462px;
    border-top: 1.5px solid var(--rule);
  }
  .entitlement { top: 415px; }
  .class-line { top: 440px; }
  .fill {
    display: inline-block;
    border-bottom: 1.5px solid var(--rule);
    font-family: "Great Vibes", cursive;
    color: var(--gold-light);
    text-align: center;
    line-height: 22px;
    vertical-align: baseline;
  }
  .fill-shares { width: 48px; font-size: 26px; }
  .fill-par { width: 160px; font-size: 26px; }
  .fill-class { width: 230px; font-size: 19px; color: var(--gold-deep); }
  .transfer { top: 490px; }
  .witness { top: 565px; }
  .signature {
    position: absolute;
    top: 689px;
    width: 140px;
    border-top: 1.5px solid var(--rule);
    padding-top: 2px;
    text-align: center;
    font-family: "Open Sans", sans-serif;
    font-style: italic;
    font-size: 20px;
  }
  .signature-left { left: 516px; }
  .signature-right { left: 786px; }
</style>
</head>
<body>
<main class="stage">
  <section class="certificate">
    <div class="world-map" role="img" aria-label="Faint grey world map spread across the background"></div>

    <svg class="frame" viewBox="0 0 1162 820" width="1162" height="820" aria-hidden="true">
      <defs>
        <linearGradient id="frameGlow" x1="0" y1="0" x2="0" y2="1">
          <stop offset="0" stop-color="#ff5a00"/>
          <stop offset="0.5" stop-color="#ffd21a"/>
          <stop offset="1" stop-color="#ff5a00"/>
        </linearGradient>
      </defs>
      <path d="M70,17 H1093 A50,50 0 0 0 1143,67 V753 A50,50 0 0 0 1093,803 H70 A50,50 0 0 0 20,753 V67 A50,50 0 0 0 70,17 Z"
            fill="none" stroke="url(#frameGlow)" stroke-width="5"/>
    </svg>

    <h1 class="title">Stock Certificate</h1>

    <div class="brand"><span class="brand-dot"></span><span>Brisk Ember</span></div>

    <p class="body-copy certifies">This certifies that</p>
    <div class="holder">Alex Marlow</div>

    <p class="body-copy entitlement">is entitled to <span class="fill fill-shares">55</span> shares of the par value of <span class="fill fill-par">1208</span>each of the</p>
    <p class="body-copy class-line"><span class="fill fill-class">Common stock</span> &nbsp;of &nbsp;the &nbsp;Brisk Ember</p>

    <p class="body-copy transfer">transferable in person or by Attorney only in the books of the Company and upon<br>the surrender of this Certificate.</p>
    <p class="body-copy witness">In witness whereof the Brisk Ember has caused this Certificate to be</p>

    <div class="signature signature-left">Signature</div>
    <div class="signature signature-right">Signature</div>
  </section>
</main>
</body>
</html>
```